Fenwick Rise Website Using Wordpress Jetpack CMS

Design a responsive SEO enabled website using Wordpress theme. 7 Pages with content to be developed. Primarily a single page site using Wordpress, so seeking a string website developer with capable skills in native understanding of SEO.

Unique Value Proposition
Sports Clubs are built on passion, people and facilities. All the volunteering and dedication in the world is limited by the level of quality services and benefits that are available to member. Access to funds and lack of knowledge create a void that holds back Club growth and access to improved facilities. Improved facilities draw members and discretionary spend to clubs, but Clubs are challenged in easily delivering expensive facility upgrades. We solve that problem in a way that's easy to digest and meets all the things considered and many that have not been considered at all!

High Level Concept
Fenwick Rise seeks to solve a growing problem. How do clubs remain viable? How do clubs increase participation? How do clubs provide exceptional value for their members discretionary expenditure?

The heart of any solid sporting club is its people, volunteers all over the world, trying to make a difference.

Fenwick Rise was built to facilitate Club growth by providing state of the art facilities without any capital exposure, in fact by providing a shared revenue model that allows for additional facilities to be layered on top of existing ones. Linking in an energy transfer scheme from the excess energy released in peak, the model allows extension to Club Member Energy Offers which exponentially grows revenues and provides strong fiscal opportunity back to the club.

At the centre of Fenwick rise are Lights and Power which are a primary life blood of every club, particularly sports clubs offering training and coaching, like tennis, soccer, rugby lawn bowls, cricket and aussie rules to name a few

With energy bills reaching in excess of $10,000 per annum in many clubs, Fenwick Rise aims to facilitate an energy performance contract for sports clubs that provides new facilities without financial exposure and a profit share on asset placement. This makes decision making easier for volunteer committees

Problems in Clubs
Membership and Participation
Attracting members and ensuring they get appropriate bang for buck takes time, energy and resources. Members seek quality environments with structured sport and easy access to sport facilities at times that suit.

Funding of Capital Assets
Clubs have considerable expenditure in infrastructure to ensure high quality facilities are upgraded and maintained.

Managing The Club
Clubs have considerable expenditure in day to day costs and unpaid volunteers are needed to maintain membership numbers and ensure high quality facilities and available.

The Solution
COST NEUTRAL INFRASTRUCTURE
Assess Power Expenditure
Identify Facilities Improvements - Value Adds etc
Provide Best Outcome Funding Model (Off Grid), Future Asset Returns, Booking/Club Mgnt
Deploy and Maintain Assets, Lower Maintenance

NEXT GEN ENERGY RETAIL SPONSORSHIP
Recover KOLR credits
Negotiate on Grid Sales
Develop Finance and Energy Rebates
Leverage Trading Mechanism

CLUB & MEMBER BENEFITS
Sponsor through Energy Purchase
Members Benefits in Offset Costs and Club Kickback
Giving Back drives the Club Improvement Plan and Income Generation + Carbon Neutral

Target Market(s)

Sports Clubs, Sports Club Committees, Local Councils looking to upgrade local club facilities

Coding

Coded - Design and coding required

Number of Pages Required

5+ page

Font styles to use
Sans Serif

Colors
acd036
848484

Requirements
Must have
• Responsive Design
• Must use Wordpress Jetpack for Delivery
• Target to use Theme with single page
• CMS for custom content additions
• Existing Domain
• Landing Pages
Nice to have
• https://www.quennary.com/en_AU/brightoak is an example of a site that displays characteristics
• Clean colour per logo and ability to expand easily using Wordpress
Should not have
• Hardcoded elements. CMS is a MUST HAVE

```html
<!DOCTYPE html>
<html lang="en">
<head>
<meta charset="utf-8">
<title>Fenwick Rise — We're the Current Specialist</title>
<link rel="stylesheet" href="https://fonts.googleapis.com/css2?family=Poppins:wght@300;400;500;600&family=Oswald:wght@500;600&display=swap">
<style>
:root{
  --green:#acd036;
  --green-dark:#96b82a;
  --grey:#848484;
  --ink:#2b2b2b;
  --muted:#8a8a8a;
  --panel:#ededed;
  --band:#7a7a7a;
  --footer:#333333;
  --footer-deep:#242424;
  --white:#ffffff;
}
*{box-sizing:border-box;margin:0;padding:0}
html,body{width:1200px;height:4206px;overflow:hidden}
body{position:relative;background:var(--white);font-family:"Poppins",Arial,sans-serif;color:var(--ink)}
.abs{position:absolute}
.btn{position:absolute;display:flex;align-items:center;justify-content:center;background:var(--green);color:var(--white);font-weight:500;text-decoration:none}
.ph{position:absolute}

/* header */
.topline{left:560px;top:0;width:640px;height:6px;background:var(--green)}
.logo{left:84px;top:34px;display:flex;align-items:center;gap:14px}
.logo-dot{width:34px;height:34px;border-radius:50%;background:var(--green)}
.logo-name{font-size:32px;font-weight:600;color:var(--green);letter-spacing:-.5px}
.contact-row{top:28px;left:574px;display:flex;align-items:center;font-size:15px;color:var(--ink);font-weight:500}
.contact-row .ico{width:22px;height:22px;border-radius:50%;background:var(--green);display:inline-flex;align-items:center;justify-content:center;margin-right:12px}
.contact-row .item{display:flex;align-items:center;margin-right:48px}
.socials{top:30px;left:984px;display:flex;gap:14px}
.socials span{width:20px;height:20px;border-radius:50%;background:var(--green)}
.nav{top:82px;left:470px;width:700px;display:flex;justify-content:space-between;font-size:14px;font-weight:500;letter-spacing:1px}
.nav a{color:var(--ink);text-decoration:none;padding:0 30px;border-left:1px solid #ccc}
.nav a:first-child{border-left:none}

/* hero */
.hero{left:0;top:123px;width:1200px;height:592px;background:linear-gradient(180deg,#4f5866 0%,#8a7a68 40%,#c7935a 62%,#4b4640 80%,#3d4a38 100%)}
.hero-title{top:310px;left:0;width:1200px;text-align:center;font-family:"Oswald",Arial,sans-serif;font-weight:600;color:var(--white);font-size:60px;line-height:72px;letter-spacing:3px}
.hero .btn{font-size:17px}

/* features */
.feature{top:743px;width:275px;height:197px;background:var(--panel);text-align:center}
.feature svg{margin-top:26px}
.feature h3{font-size:20px;font-weight:500;margin-top:10px}
.feature p{font-size:12px;color:var(--muted);line-height:20px;margin:10px 24px 0}

/* welcome */
.welcome-kicker{left:84px;top:1018px;font-size:22px;font-weight:400;letter-spacing:2px}
.welcome-title{left:84px;top:1052px;font-size:38px;font-weight:400;letter-spacing:3px}
.welcome-rule{left:358px;top:1090px;width:104px;height:1px;background:#bbb}
.welcome-text{left:84px;top:1130px;width:440px;font-size:14px;line-height:25px;color:var(--muted)}
.welcome-photo{left:617px;top:987px;width:583px;height:348px;background:linear-gradient(180deg,#4a5563 0%,#2f3844 55%,#3b3a2e 80%,#4d5a3a 100%)}

/* section heading */
.sec-title{left:0;width:1200px;text-align:center;font-size:40px;font-weight:400;letter-spacing:4px}
.sec-rule{height:1px;background:#bbb;width:112px}

/* specs */
.spec{width:260px;font-size:14px;line-height:20px;color:var(--ink)}
.spec b{display:block;font-weight:500;font-size:14px;letter-spacing:.5px;text-transform:uppercase;margin-bottom:4px}
.spec span{color:#555;font-size:12.5px;line-height:19px;display:block}
.product{left:435px;top:1584px;width:265px;height:463px;background:linear-gradient(100deg,#ffffff 0%,#f0f0f0 75%,#2a2a2a 90%,#111 100%);box-shadow:0 18px 30px rgba(0,0,0,.2)}

/* call band */
.callband{left:0;top:2117px;width:1200px;height:104px;background:var(--green);color:var(--white)}
.callband .txt{top:32px;font-size:30px;font-weight:400}
.callband .div{top:22px;width:1px;height:60px;background:rgba(255,255,255,.6)}
.or{left:544px;top:21px;width:62px;height:62px;border-radius:50%;background:#c3e06a;display:flex;align-items:center;justify-content:center;font-size:18px}

/* works */
.work{top:2434px;width:238px}
.work .ph{position:relative;height:188px}
.work h4{font-size:19px;font-weight:500;text-align:center;margin-top:22px}
.work p{font-size:12px;color:var(--muted);text-align:center;line-height:20px;margin-top:14px;padding:0 40px}
.work .btn{position:relative;margin:18px auto 0;width:134px;height:38px;border-radius:19px;font-size:13px}

/* testimonial */
.quote-band{left:0;top:2967px;width:1200px;height:188px;background:var(--band);color:var(--white);text-align:center}
.quote-band p{position:absolute;top:86px;left:120px;width:960px;font-size:15px;line-height:25px}
.quote-band .who{top:143px;left:0;width:1200px;font-size:12px;letter-spacing:1px}
.quote-band .who em{font-style:normal;color:var(--green)}
.avatar{left:533px;top:2900px;width:134px;height:134px;border-radius:50%;border:5px solid var(--white);background:linear-gradient(180deg,#c9b8a6,#8a7562)}

/* blog */
.post{top:3379px;width:325px;height:340px}
.post .ph{left:0;top:0;width:325px;height:204px}
.post .card{position:absolute;left:17px;top:175px;width:291px;height:150px;background:var(--white);box-shadow:0 2px 8px rgba(0,0,0,.08);padding:14px 18px}
.post h4{font-size:20px;font-weight:500}
.post .card i{display:block;width:36px;height:2px;background:var(--green);margin:6px 0 14px}
.post p{font-size:12px;color:var(--muted);line-height:20px}

/* footer */
.footer{left:0;top:3814px;width:1200px;height:336px;background:var(--footer);color:#ddd}
.footer h5{position:absolute;top:70px;font-size:12px;font-weight:500;letter-spacing:1px;color:var(--white)}
.f-line{position:absolute;font-size:12.5px;line-height:20px;color:#ddd}
.f-ico{position:absolute;width:24px;height:24px;border-radius:50%;background:#555;display:flex;align-items:center;justify-content:center}
.f-post b{display:block;font-weight:500;color:var(--white)}
.f-post small{display:block;font-size:10.5px;color:#999}
.field{position:absolute;left:810px;width:244px;height:30px;border:1px solid #888;background:transparent;font-size:11px;color:#aaa;padding:7px 10px}
.submit{left:810px;top:260px;width:244px;height:28px;font-size:14px}
.bottom{left:0;top:4150px;width:1200px;height:56px;background:var(--footer-deep);color:#999;font-size:11px;text-align:center;line-height:56px}
</style>
</head>
<body>

<header>
  <div class="abs topline"></div>
  <div class="abs logo"><span class="logo-dot"></span><span class="logo-name">Fenwick Rise</span></div>
  <div class="abs contact-row">
    <div class="item"><span class="ico"><svg width="12" height="9" viewBox="0 0 12 9"><rect x=".5" y=".5" width="11" height="8" fill="none" stroke="#fff"/><path d="M.5 .5 6 5l5.5-4.5" fill="none" stroke="#fff"/></svg></span>info@fenwickrise.com</div>
    <div class="item"><span class="ico"><svg width="10" height="10" viewBox="0 0 10 10"><path d="M2 1l2 2-1 1.5c.7 1.3 1.2 1.8 2.5 2.5L7 6l2 2-1.2 1.5C4.5 9 1 5.5.5 2.2z" fill="#fff"/></svg></span>646-555-0174</div>
  </div>
  <div class="abs socials"><span></span><span></span><span></span><span></span></div>
  <nav class="abs nav"><a href="#">FENWICK RISE</a><a href="#">SOLAR PROOF</a><a href="#">COMMERCIAL</a><a href="#">UTILITIES</a></nav>
</header>

<section class="abs hero" role="img" aria-label="Modern house with lit garage and driveway at sunset"></section>
<h1 class="abs hero-title">WE'RE THE<br>CURRENT SPECIALIST!</h1>
<a class="btn" href="#" style="left:415px;top:490px;width:168px;height:50px;font-size:17px">KNOW MORE</a>
<a class="btn" href="#" style="left:617px;top:490px;width:163px;height:50px;font-size:17px">CONTACT US</a>

<section>
  <div class="abs feature" style="left:0">
    <svg width="40" height="50" viewBox="0 0 40 50"><path d="M24 2 8 28h12l-4 20 16-28H20z" fill="none" stroke="#888" stroke-width="1.5"/></svg>
    <h3>Power Energy</h3><p>Lorem Ipsum is simply dummy text of the printing and typesetting.</p></div>
  <div class="abs feature" style="left:308px">
    <svg width="50" height="50" viewBox="0 0 50 50"><path d="M4 18h30a6 6 0 1 0-6-6M4 26h38a5 5 0 1 1-5 5M4 34h22" fill="none" stroke="#888" stroke-width="1.5"/></svg>
    <h3>Wind Energy</h3><p>Lorem Ipsum is simply dummy text of the printing and typesetting.</p></div>
  <div class="abs feature" style="left:617px">
    <svg width="50" height="50" viewBox="0 0 50 50"><path d="M8 42 30 20M34 8a8 8 0 0 0 8 12L36 14zM10 8l30 32M6 44l4-4" fill="none" stroke="#888" stroke-width="1.5"/></svg>
    <h3>Easy Support</h3><p>Lorem Ipsum is simply dummy text of the printing and typesetting.</p></div>
  <div class="abs feature" style="left:925px">
    <svg width="50" height="50" viewBox="0 0 50 50"><circle cx="25" cy="24" r="10" fill="none" stroke="#888" stroke-width="1.5"/><path d="M25 4v6M25 38v6M5 24h6M39 24h6M11 10l4 4M35 34l4 4M39 10l-4 4M15 34l-4 4" stroke="#888" stroke-width="1.5"/></svg>
    <h3>Reduced Costs</h3><p>Lorem Ipsum is simply dummy text of the printing and typesetting.</p></div>
</section>

<section>
  <div class="abs welcome-kicker">WELCOME TO</div>
  <h2 class="abs welcome-title">FENWICK RISE</h2>
  <div class="abs welcome-rule" style="left:396px"></div>
  <p class="abs welcome-text">Lorem ipsum dolor sit amet, consectetur adipiscing elit, sed do eiusmod tempor incididunt ut labore et dolore magna aliqua. Ut enim ad minim veniam, quis nostrud exercitation ullamco laboris nisi ut aliquip ex ea commodo consequat.</p>
  <a class="btn" href="#" style="left:84px;top:1270px;width:205px;height:56px;border-radius:28px;font-size:18px">Learn More</a>
  <div class="abs welcome-photo" role="img" aria-label="House with warm lit windows at dusk"></div>
</section>

<section>
  <div class="abs sec-rule" style="left:280px;top:1486px"></div>
  <h2 class="abs sec-title" style="top:1458px">TECHNICAL SPECS</h2>
  <div class="abs sec-rule" style="left:808px;top:1486px"></div>

  <svg class="abs" style="left:351px;top:1571px" width="448" height="448" viewBox="0 0 448 448"><circle cx="224" cy="224" r="222" fill="none" stroke="#f0f0f0" stroke-width="3"/><circle cx="224" cy="224" r="180" fill="none" stroke="#e6e6e6" stroke-width="14"/></svg>
  <div class="abs product" role="img" aria-label="Wall-mounted home battery unit"></div>

  <div class="abs spec" style="left:123px;top:1622px"><b>Usable Capacity</b><span>13.5 kWh</span></div>
  <div class="abs spec" style="left:123px;top:1678px"><b>Depth of Discharge</b><span>100%</span></div>
  <div class="abs spec" style="left:123px;top:1734px"><b>Efficiency</b><span>90% round-trip</span></div>
  <div class="abs spec" style="left:123px;top:1788px"><b>Power</b><span>7kW peak / 5kW continuous</span></div>
  <div class="abs spec" style="left:123px;top:1842px"><b>Supported Applications</b><span>Solar self-consumption<br>Back-up power<br>Time-Based control<br>Off-grid capabilities (coming soon)</span></div>
  <div class="abs spec" style="left:123px;top:1956px"><b>Warranty</b><span>10 years</span></div>

  <div class="abs spec" style="left:860px;top:1612px"><b>Scalable</b><span>Up to 10 Brightoak units</span></div>
  <div class="abs spec" style="left:860px;top:1668px"><b>Operating Temperature</b><span>-4°F to 122°F / -20°C to 50°C</span></div>
  <div class="abs spec" style="left:860px;top:1724px"><b>Dimensions</b><span>L x W x D: 44" x 29" x 5.5"<br>(1150mm x 755mm x 155mm)</span></div>
  <div class="abs spec" style="left:860px;top:1798px"><b>Weight</b><span>125 kg</span></div>
  <div class="abs spec" style="left:860px;top:1852px"><b>Installation</b><span>Floor or wall mounted<br>Indoor or outdoor</span></div>
  <div class="abs spec" style="left:860px;top:1926px"><b>Certification</b><span>North American and International Standards<br>Grid code compliant</span></div>
</section>

<section class="abs callband">
  <svg class="abs" style="left:86px;top:30px" width="26" height="44" viewBox="0 0 26 44"><rect x="1.5" y="1.5" width="23" height="41" rx="3" fill="none" stroke="#fff" stroke-width="2"/><path d="M10 37h6" stroke="#fff" stroke-width="2"/></svg>
  <div class="abs div" style="left:134px"></div>
  <div class="abs txt" style="left:166px">Call Us : 336-555-0138</div>
  <div class="abs or">OR</div>
  <svg class="abs" style="left:686px;top:38px" width="46" height="30" viewBox="0 0 46 30"><rect x="1" y="1" width="44" height="28" fill="none" stroke="#fff" stroke-width="2"/><path d="M1 1l22 16L45 1" fill="none" stroke="#fff" stroke-width="2"/></svg>
  <div class="abs div" style="left:734px"></div>
  <div class="abs txt" style="left:766px">Mail Us : <span style="font-size:24px">info@fenwickrise.com</span></div>
</section>

<section>
  <div class="abs sec-rule" style="left:332px;top:2336px"></div>
  <h2 class="abs sec-title" style="top:2308px">OUR WORKS</h2>
  <div class="abs sec-rule" style="left:756px;top:2336px"></div>

  <article class="abs work" style="left:84px"><div class="ph" role="img" aria-label="Electrician fitting a wall socket" style="background:linear-gradient(135deg,#e9e4dc,#c9b79b)"></div><h4>Lorem Ipsum Dummy</h4><p>we provide the space, client pays for services</p><a class="btn" href="#">Learn More</a></article>
  <article class="abs work" style="left:348px"><div class="ph" role="img" aria-label="Electrician's hand tools laid out" style="background:linear-gradient(135deg,#d8d8d8,#8c7a62)"></div><h4>Lorem Ipsum Dummy</h4><p>we provide the space, client pays for services</p><a class="btn" href="#">Learn More</a></article>
  <article class="abs work" style="left:612px"><div class="ph" role="img" aria-label="Worker with tool belt and cable coil" style="background:linear-gradient(135deg,#c43d3a,#3b4a6b)"></div><h4>Lorem Ipsum Dummy</h4><p>we provide the space, client pays for services</p><a class="btn" href="#">Learn More</a></article>
  <article class="abs work" style="left:876px"><div class="ph" role="img" aria-label="Electrician working at a switchboard" style="background:linear-gradient(135deg,#b9c4cc,#3e5f8a)"></div><h4>Lorem Ipsum Dummy</h4><p>we provide the space, client pays for services</p><a class="btn" href="#">Learn More</a></article>
</section>

<section>
  <div class="abs quote-band">
    <p>An entity which provides insurance is known as an insurer, insurance company, or insurance carrier. A person or entity who buys insurance is known as an insured or policyholder. The action involves a contract.</p>
    <div class="abs who">DANA WHITLOW, <em>MANAGER</em></div>
  </div>
  <div class="abs avatar" role="img" aria-label="Client portrait"></div>
</section>

<section>
  <div class="abs sec-rule" style="left:336px;top:3275px"></div>
  <h2 class="abs sec-title" style="top:3247px">OUR BLOG</h2>
  <div class="abs sec-rule" style="left:752px;top:3275px"></div>

  <article class="abs post" style="left:84px"><div class="ph" role="img" aria-label="Worker with tool belt and cable" style="background:linear-gradient(135deg,#c43d3a,#33405c)"></div><div class="card"><h4>Lorem Ipsum</h4><i></i><p>Contrary to popular belief, Lorem Ipsum is not simply random text. It has roots in a piece...</p></div></article>
  <article class="abs post" style="left:437px"><div class="ph" role="img" aria-label="Electrician wiring a socket" style="background:linear-gradient(135deg,#f1ede6,#b9a58a)"></div><div class="card"><h4>Lorem Ipsum</h4><i></i><p>Contrary to popular belief, Lorem Ipsum is not simply random text. It has roots in a piece...</p></div></article>
  <article class="abs post" style="left:790px"><div class="ph" role="img" aria-label="Electrician at a switchboard" style="background:linear-gradient(135deg,#c0c9d0,#3e5f8a)"></div><div class="card"><h4>Lorem ipsum</h4><i></i><p>Contrary to popular belief, Lorem Ipsum is not simply random text. It has roots in a piece...</p></div></article>
</section>

<footer class="abs footer">
  <h5 style="left:143px">CONTACT INFORMATION</h5>
  <div class="f-ico" style="left:143px;top:124px"><svg width="10" height="14" viewBox="0 0 10 14"><path d="M5 13S1 8 1 5a4 4 0 0 1 8 0c0 3-4 8-4 8z" fill="#fff"/></svg></div>
  <div class="f-line" style="left:192px;top:118px">Fenwick Rise<br>48 Larchmont Way<br>Elmridge, NC 27990</div>
  <div class="f-ico" style="left:143px;top:210px"><svg width="10" height="10" viewBox="0 0 10 10"><path d="M2 1l2 2-1 1.5c.7 1.3 1.2 1.8 2.5 2.5L7 6l2 2-1.2 1.5C4.5 9 1 5.5.5 2.2z" fill="#fff"/></svg></div>
  <div class="f-line" style="left:192px;top:212px">336-555-0138</div>
  <div class="f-ico" style="left:143px;top:266px"><svg width="12" height="9" viewBox="0 0 12 9"><rect x=".5" y=".5" width="11" height="8" fill="none" stroke="#fff"/><path d="M.5 .5 6 5l5.5-4.5" fill="none" stroke="#fff"/></svg></div>
  <div class="f-line" style="left:192px;top:268px">info@fenwickrise.com</div>

  <h5 style="left:460px">RECENT BLOG POSTS</h5>
  <div class="f-line f-post" style="left:460px;top:116px;width:300px"><b>Nulla consequat massa quis enim</b><small>November 19, 2016</small>The sight of the tumblers restored Bob ...</div>
  <div class="f-line f-post" style="left:460px;top:210px;width:300px"><b>Nulla consequat massa quis enim</b><small>November 19, 2016</small>The sight of the tumblers restored Bob ...</div>

  <h5 style="left:810px">CONTACT US</h5>
  <div class="field" style="top:128px">Name...</div>
  <div class="field" style="top:173px">Email...</div>
  <div class="field" style="top:218px">Phone No...</div>
  <a class="btn submit" href="#">Submit</a>
</footer>
<div class="abs bottom">fenwickrise.com 2017. All rights reserved</div>

</body>
</html>
```